Re-design / re-work of existing website

Need to re-design a website so it's easy for me as a user to update/add pictures and change descriptions.

If possible, would there be a way to display LodgeVista calendars? We have 3 cottages and it would be ideal to have each cottage with pics on one page along with a readonly version of the LodgeVista calendar plugin (if such a thing exists) so that visitors to the site can see what is available and what is not.

Existing site: http://tarnwoodlets.net

```html
<!DOCTYPE html>
<html lang="en">
<head>
<meta charset="utf-8">
<title>Tarnwood Cottages</title>
<link href="https://fonts.googleapis.com/css2?family=Poppins:wght@400;500;600&display=swap" rel="stylesheet">
<style>
:root{
  --ink:#1f1f1f;
  --dark:#2f2f2f;
  --btn:#484444;
  --panel:#f2f0f0;
  --band:#ebebeb;
  --explore:#f5f5f5;
  --footer:#2a2a2a;
  --copy:#3a3a3a;
}
*{box-sizing:border-box;margin:0;padding:0}
html,body{width:1200px;height:4573px;overflow:hidden}
body{position:relative;font-family:'Poppins',sans-serif;color:var(--ink);background:#fff}
.abs{position:absolute}
.topbar{left:0;top:0;width:1200px;height:83px;background:var(--dark);color:#fff;font-size:16px}
.topbar .contact{position:absolute;top:29px;display:flex;align-items:center;gap:10px}
.topbar .divider{position:absolute;left:596px;top:26px;width:1px;height:32px;background:#888}
.topbar .cta{position:absolute;left:907px;top:18px;width:209px;height:48px;border:1px solid #bbb;display:flex;align-items:center;justify-content:center;font-size:16px}
.navbar{left:0;top:83px;width:1200px;height:109px;background:#fff}
.brand{position:absolute;left:86px;top:40px;font-size:19px;font-weight:500;color:var(--ink);display:flex;align-items:center;gap:8px}
.brand .dot{width:10px;height:10px;border-radius:50%;background:var(--ink)}
.nav{position:absolute;top:47px;font-size:14px;color:#444}
.hero{left:0;top:192px;width:1200px;height:541px;background:linear-gradient(160deg,#7c8a6e 0%,#a9a8a0 35%,#c9c6bd 55%,#6f7c5a 80%,#23303c 100%)}
.booking{left:131px;top:541px;width:952px;height:446px;background:var(--panel)}
.mark{position:absolute;font-size:15px;font-weight:500;letter-spacing:1px;text-transform:uppercase;color:var(--ink);text-align:center}
.booking h1{position:absolute;left:0;width:100%;top:110px;text-align:center;font-size:39px;font-weight:600}
.booking p{position:absolute;left:0;width:100%;top:172px;text-align:center;font-size:15px}
.field{position:absolute;background:#fff;border:1px solid #e2e0e0;display:flex;align-items:center;padding-left:26px;font-size:16px}
.field .tail{position:absolute;right:0;top:0;height:100%;width:56px;border-left:1px solid #e2e0e0;display:flex;align-items:center;justify-content:center}
.search{position:absolute;background:var(--btn);color:#fff;display:flex;align-items:center;justify-content:center;font-size:17px}
.photo{position:absolute}
.cottage-head{position:absolute;text-align:center}
.cottage-head h2{font-size:42px;font-weight:600;line-height:1}
.cottage-head .sub{font-size:25px;line-height:30px;margin-top:30px}
.sleep{position:absolute;display:flex;align-items:center;justify-content:center;gap:10px;font-size:15px;font-weight:600}
.sleep .rule{height:2px;background:var(--ink);position:relative;flex:1}
.sleep .rule::before{content:"";position:absolute;top:-3px;width:8px;height:8px;border-radius:50%;background:var(--ink)}
.sleep .rule.l::before{left:0}.sleep .rule.r::before{right:0}
.beds{position:absolute;text-align:center;font-size:15px;line-height:21px}
.btn-outline{position:absolute;border:3px solid #3a3a3a;background:#fff;display:flex;align-items:center;justify-content:center;font-size:21px;color:#555}
.btn-solid{position:absolute;background:var(--btn);color:#fff;display:flex;align-items:center;justify-content:center;font-size:21px}
.band{left:0;top:1692px;width:1200px;height:640px;background:var(--band)}
.explore{left:0;top:3009px;width:1200px;height:1148px;background:var(--explore)}
.explore-title{left:0;width:1200px;top:3155px;text-align:center;font-size:42px;font-weight:600}
.tile{position:absolute;width:329px;height:354px}
.tile span{position:absolute;left:0;bottom:26px;width:100%;text-align:center;color:#fff;font-size:20px;font-weight:500}
.footer{left:0;top:4157px;width:1200px;height:336px;background:var(--footer)}
.footer-brand{position:absolute;left:86px;top:4258px;font-size:24px;font-weight:500;color:#fff;display:flex;align-items:center;gap:10px}
.footer-brand .dot{width:12px;height:12px;border-radius:50%;background:#fff}
.newsletter{left:650px;top:4253px;width:468px;height:75px;background:#d9d9d9}
.newsletter .ph{position:absolute;left:32px;top:27px;font-size:15px;color:#555}
.newsletter .go{position:absolute;left:303px;top:9px;width:155px;height:55px;background:#1e1e1e;color:#fff;display:flex;align-items:center;justify-content:center;font-size:15px}
.flinks{left:0;top:4393px;width:1200px;display:flex;justify-content:center;color:#fff;font-size:16px}
.flinks a{color:#fff;text-decoration:none;padding:0 27px;border-left:1px solid #bbb;line-height:36px}
.flinks a:first-child{border-left:none}
.copyright{left:0;top:4493px;width:1200px;height:80px;background:var(--copy);color:#fff;font-size:15px;display:flex;align-items:center;justify-content:center}
</style>
</head>
<body>

<header class="abs topbar">
  <div class="contact" style="left:420px">
    <svg width="18" height="18" viewBox="0 0 24 24" fill="none" stroke="#fff" stroke-width="2"><path d="M5 3h4l2 5-3 2a12 12 0 0 0 6 6l2-3 5 2v4a2 2 0 0 1-2 2A18 18 0 0 1 3 5a2 2 0 0 1 2-2z"/></svg>
    <span>+1 555 014 2926</span>
  </div>
  <div class="divider"></div>
  <div class="contact" style="left:628px">
    <svg width="22" height="16" viewBox="0 0 22 16" fill="#fff"><rect x="0" y="0" width="22" height="16" rx="1"/><path d="M1 1l10 8 10-8" stroke="#2f2f2f" stroke-width="2" fill="none"/></svg>
    <span>support@tarnwoodlets.net</span>
  </div>
  <div class="cta">Check Availability</div>
</header>

<nav class="abs navbar">
  <div class="brand"><span class="dot"></span>Tarnwood Cottages</div>
  <span class="nav" style="left:320px">Home</span>
  <span class="nav" style="left:400px">Our Cottages</span>
  <span class="nav" style="left:530px">Adventures</span>
  <span class="nav" style="left:658px">Getting Here</span>
  <span class="nav" style="left:790px">Contact Us</span>
  <span class="nav" style="left:919px">Today's Weather</span>
  <span class="nav" style="left:1066px">Policies</span>
</nav>

<div class="abs hero" role="img" aria-label="Aerial photo of the lakeside cottages on granite shoreline with pine trees"></div>

<section class="abs booking">
  <div class="mark" style="left:560px;top:68px">Tarnwood</div>
  <h1>Check Availability of Cottages</h1>
  <p>Discover entire homes and rooms perfect for any trip.</p>
  <div class="field" style="left:135px;top:231px;width:282px;height:66px">Select Cottage
    <div class="tail"><svg width="14" height="10"><path d="M0 0h14L7 10z" fill="#666"/></svg></div></div>
  <div class="field" style="left:428px;top:231px;width:179px;height:66px">Check &nbsp;In
    <div class="tail" style="width:42px"><svg width="18" height="18" viewBox="0 0 18 18" fill="none" stroke="#444" stroke-width="1.6"><rect x="1" y="3" width="16" height="14"/><path d="M1 7h16M5 1v4M13 1v4M5 10h2M9 10h2M13 10h1M5 13h2M9 13h2"/></svg></div></div>
  <div class="field" style="left:618px;top:231px;width:181px;height:66px">Check Out
    <div class="tail" style="width:42px"><svg width="18" height="18" viewBox="0 0 18 18" fill="none" stroke="#444" stroke-width="1.6"><rect x="1" y="3" width="16" height="14"/><path d="M1 7h16M5 1v4M13 1v4M5 10h2M9 10h2M13 10h1M5 13h2M9 13h2"/></svg></div></div>
  <div class="field" style="left:135px;top:320px;width:181px;height:64px">Adults
    <div class="tail" style="width:50px"><svg width="14" height="10"><path d="M0 0h14L7 10z" fill="#666"/></svg></div></div>
  <div class="field" style="left:331px;top:320px;width:179px;height:64px">Children
    <div class="tail" style="width:50px"><svg width="14" height="10"><path d="M0 0h14L7 10z" fill="#666"/></svg></div></div>
  <div class="search" style="left:524px;top:320px;width:275px;height:64px">Search</div>
</section>

<!-- The Willow -->
<div class="photo" style="left:89px;top:1049px;width:449px;height:426px;background:linear-gradient(150deg,#e6e2da 0%,#c79b6c 35%,#a8774c 65%,#7d5a42 100%)" role="img" aria-label="Photo of the Willow living room with pine walls, sofas and coffee table"></div>
<div class="mark" style="left:752px;top:1110px;width:200px">Tarnwood</div>
<div class="cottage-head" style="left:600px;top:1176px;width:504px">
  <h2>The Willow</h2>
  <div class="sub">3 Bedroom, 1 Bathroom with<br>Large Kitchen and Living Space</div>
</div>
<div class="sleep" style="left:627px;top:1355px;width:466px"><span class="rule l"></span>Sleeping Configuration:<span class="rule r"></span></div>
<div class="beds" style="left:600px;top:1396px;width:504px">Master Bedroom - Queen | Second Bedroom - Single + Double<br>Third Bedroom - Bunk Bed (Double below and single above)</div>
<div class="btn-outline" style="left:85px;top:1516px;width:455px;height:87px">View All Images</div>
<div class="btn-solid" style="left:625px;top:1518px;width:449px;height:83px">Check Availability</div>

<!-- The Maple -->
<div class="abs band"></div>
<div class="mark" style="left:207px;top:1775px;width:200px">Tarnwood</div>
<div class="cottage-head" style="left:60px;top:1837px;width:495px">
  <h2>The Maple</h2>
  <div class="sub" style="margin-top:26px">3 Bedroom, 2 Bathrooms with Large<br>Kitchen and Living Space</div>
</div>
<div class="beds" style="left:60px;top:1987px;width:495px;font-weight:600">Sleeping Configuration:</div>
<div class="beds" style="left:60px;top:2028px;width:495px">Master Bedroom - Queen | Second Bedroom - Double<br>Third Bedroom - Two Single</div>
<div class="btn-solid" style="left:82px;top:2157px;width:451px;height:83px">Check Availability</div>
<div class="photo" style="left:650px;top:1803px;width:456px;height:334px;background:linear-gradient(130deg,#9a9a96 0%,#b98a5c 30%,#7a3e26 60%,#d8dde2 100%)" role="img" aria-label="Photo of the Maple living room with leather sofa and patio doors"></div>
<div class="btn-outline" style="left:650px;top:2155px;width:456px;height:87px">View All Images</div>

<!-- The Spruce -->
<div class="photo" style="left:92px;top:2441px;width:446px;height:333px;background:linear-gradient(120deg,#b6bfc8 0%,#c8a376 35%,#8a6448 65%,#5e8d9b 100%)" role="img" aria-label="Photo of the Spruce dining area with wooden table and kitchen"></div>
<div class="mark" style="left:775px;top:2494px;width:200px">Tarnwood</div>
<div class="cottage-head" style="left:623px;top:2555px;width:504px">
  <h2>The Spruce</h2>
  <div class="sub">2 Bedroom, 1 Bathroom with<br>Large Kitchen and Living Space</div>
</div>
<div class="sleep" style="left:635px;top:2706px;width:466px"><span class="rule l"></span>Sleeping Configuration:<span class="rule r"></span></div>
<div class="beds" style="left:623px;top:2747px;width:504px">Master Bedroom - Queen | Second Bedroom - Double</div>
<div class="btn-outline" style="left:89px;top:2821px;width:454px;height:88px">View All Images</div>
<div class="btn-solid" style="left:653px;top:2824px;width:449px;height:83px">Check Availability</div>

<!-- Explore -->
<section class="abs explore"></section>
<div class="mark" style="left:855px;top:3085px;width:200px">Tarnwood</div>
<h2 class="abs explore-title">Things to Explore near Tarnwood Cottages</h2>

<div class="tile" style="left:85px;top:3294px;background:linear-gradient(170deg,#4a5a8c 0%,#2b2f4a 40%,#8a5a2a 70%,#3a2a20 100%)" role="img" aria-label="Photo of the visitor centre building lit at dusk"><span>Riverside Visitor Centre</span></div>
<div class="tile" style="left:435px;top:3294px;background:linear-gradient(180deg,#4e6a3a 0%,#6d8a52 40%,#dfe3e3 62%,#5a5f5c 100%)" role="img" aria-label="Photo of rapids and waterfall with forest"><span>Cedar Run Falls</span></div>
<div class="tile" style="left:785px;top:3294px;background:linear-gradient(180deg,#c3cad0 0%,#5d4a44 35%,#6a5048 65%,#4a4a4a 100%)" role="img" aria-label="Photo of a rustic trading post shop with flower boxes"><span>Riverbend Trading Post</span></div>
<div class="tile" style="left:85px;top:3706px;background:linear-gradient(180deg,#8a9098 0%,#2e3b2c 40%,#9aa0a6 65%,#3c4038 100%)" role="img" aria-label="Photo of a calm lake reflecting forest in a provincial park"><span>Stonelake Provincial Park</span></div>
<div class="tile" style="left:435px;top:3706px;background:linear-gradient(180deg,#b9c1c6 0%,#6f7479 35%,#545a55 70%,#3a3d3a 100%)" role="img" aria-label="Photo of a marina dock with canoes and kayaks"><span>Tarnwood Bay Marina</span></div>
<div class="tile" style="left:785px;top:3706px;background:linear-gradient(180deg,#c9cfd4 0%,#e6d3b0 40%,#8e3a3e 70%,#4a3a34 100%)" role="img" aria-label="Photo of red lawn chairs on a rocky point at sunset"><span>Pinepoint Park</span></div>

<!-- Footer -->
<footer class="abs footer"></footer>
<div class="footer-brand"><span class="dot"></span>Tarnwood Cottages</div>
<div class="abs newsletter"><span class="ph">Enter Your Email Address</span><div class="go">Sign Up</div></div>
<div class="abs flinks">
  <a href="#">Our Cottages</a><a href="#">Adventures</a><a href="#">Getting Here</a><a href="#">Contact Us</a><a href="#">Today's Weather</a><a href="#">Policies</a>
</div>
<div class="abs copyright">Copyright @ 2023 All rights reserved</div>

</body>
</html>
```